Dental Design, very professional and noticable

Tindale Ridge Dental Surgery is based in Pelican Waters. We are a fast growing dental surgery and are looking for some professional business cards to send to patients.
We would like to see a design that is Vertical and uses the colours Soft Blue, Silver, White and Black. Maybe a full blue side with moto and details on back? Any other ideas or colours that you may think will make the card look unique is fine.
We need all details on the card that are listed above

Target Market(s)

Families, Retired, Other Professionals and Businesses

Industry/Entity Type

Dental

Contact Information for Business Card

Tindale Ridge Dental Surgery
Family, Cosmetic, Preventative
Dr. Owen Castrey
Dental Surgeon
BDS (Adel) FAE FADI FICD FPFA
phone: (07)50001846
fax: (07)50002917
email: tindaleridgedental@quillpost.com
http://tindaleridgedental.com/

Logo Text

Logo styles of interest
Abstract Logo
Requirements
Must have
• Vertical, Vibrant but Professional, Rounded Edges, Logo on front and back of card (different colours on each side)
Nice to have
• One side completely blue (not sure what shade) with logo and moto on bottom
Other side white, with blue or different coloured logo with details in black and silver?
Logo should show half circle with 1 end as arrow symbolizing pelican waters canal also a magnifine glass also half circled with 1 end as arrow. Any other ideas are welcome.
Should not have
• A tooth. A smile. Toothbrush or Toothpaste. Cornered edges.

```html
<!DOCTYPE html>
<html lang="en">
<head>
<meta charset="utf-8">
<title>Tindale Ridge Dental Surgery – Business Cards</title>
<link href="https://fonts.googleapis.com/css2?family=Arimo:wght@400;700&family=Marcellus&display=swap" rel="stylesheet">
<style>
  :root {
    --backdrop: #202020;
    --navy: #0f1f5c;
    --navy-deep: #0a1540;
    --royal: #1b4a8f;
    --gold: #96782a;
    --gold-text: #a07c25;
    --white: #ffffff;
    --ink: #111111;
    --label-blue: #2a3f9a;
  }
  * { margin: 0; padding: 0; box-sizing: border-box; }
  html, body {
    width: 1200px; height: 1200px; overflow: hidden;
    background: var(--backdrop);
  }
  .sheet {
    position: relative; width: 1200px; height: 1200px;
  }
  .card {
    position: absolute; left: 170px; width: 860px; height: 490px;
    border-radius: 18px; overflow: hidden;
  }
  /* ---------- Front: details side ---------- */
  .card--front { top: 80px; background: var(--white); }
  .brand {
    position: absolute; left: 60px; top: 150px; width: 330px;
  }
  .brand__mark {
    width: 34px; height: 34px; border-radius: 50%;
    background: var(--gold); margin-bottom: 16px;
  }
  .brand__name {
    font-family: "Marcellus", serif; font-size: 30px; line-height: 1.15;
    color: var(--gold-text);
  }
  .brand__tagline {
    font-family: "Marcellus", serif; font-size: 21px;
    color: var(--gold-text); margin-top: 12px;
  }
  .contact {
    position: absolute; left: 430px; top: 58px; width: 400px;
    font-family: "Arimo", sans-serif; color: var(--ink);
  }
  .contact__name {
    font-weight: 700; font-size: 34px; color: var(--navy);
  }
  .contact__role {
    font-weight: 700; font-size: 11px; margin-top: 4px; letter-spacing: .2px;
  }
  .contact__list { list-style: none; margin-top: 26px; font-size: 19px; line-height: 1.6; }
  .contact__label { color: var(--label-blue); }
  .stripes {
    position: absolute; left: 0; bottom: 0; width: 100%; height: 104px;
    background: linear-gradient(90deg, var(--navy-deep), var(--navy) 50%, var(--navy-deep));
  }
  .stripes__gold {
    position: absolute; left: 0; top: 36px; width: 100%; height: 28px;
    background: var(--gold);
  }
  /* ---------- Back: brand side ---------- */
  .card--back { top: 630px; background: var(--white); }
  .back__field {
    position: absolute; left: 0; top: 0; width: 100%; height: 380px;
    background: radial-gradient(ellipse 60% 75% at 58% 40%, #1f5c9e 0%, var(--royal) 30%, var(--navy) 70%, var(--navy-deep) 100%);
  }
  .back__mark {
    position: absolute; left: 50%; top: 120px; transform: translateX(-50%);
    width: 70px; height: 70px; border-radius: 50%; background: var(--white);
  }
  .back__name {
    position: absolute; left: 0; width: 100%; top: 275px; text-align: center;
    font-family: "Marcellus", serif; font-size: 52px; color: var(--white);
  }
  .back__tagline {
    position: absolute; left: 0; width: 100%; top: 392px; text-align: center;
    font-family: "Marcellus", serif; font-size: 40px; color: var(--royal);
  }
</style>
</head>
<body>
<main class="sheet">
  <section class="card card--front" aria-label="Card front with contact details">
    <div class="brand">
      <div class="brand__mark"></div>
      <p class="brand__name">Tindale Ridge Dental Surgery</p>
      <p class="brand__tagline">Family, Cosmetic, Preventive</p>
    </div>
    <div class="contact">
      <h1 class="contact__name">Dr. Owen Castrey</h1>
      <p class="contact__role">Dental Surgeon BDS (Adel) FAE FADI FICD FPFA</p>
      <ul class="contact__list">
        <li><span class="contact__label">Phone:</span> (07)50001846</li>
        <li><span class="contact__label">Fax:</span> (07)50002917</li>
        <li>tindaleridgedental@quillpost.com</li>
        <li>www.tindaleridgedental.com</li>
      </ul>
    </div>
    <div class="stripes"><div class="stripes__gold"></div></div>
  </section>

  <section class="card card--back" aria-label="Card back with practice name">
    <div class="back__field"></div>
    <div class="back__mark"></div>
    <p class="back__name">Tindale Ridge Dental Surgery</p>
    <p class="back__tagline">Family, Cosmetic, Preventive</p>
  </section>
</main>
</body>
</html>
```